GREEN WILLOW LICE REMOVAL labels

I need a label design for our MINT REPELLING SHAMPOO (LICE PREVENTION).
It also includes our MINT REPELLING CONDITIONER (LICE PREVENTION) and our MINT SPRAY (LICE PREVENTION) also includes LICE & NIT ELIMINATING MOUSSE (LICE TREATMENT) and a LICE ELIMINATOR 100% Dimethicone oil (LICE TREATMENT). The shampoo and conditioner are sulfate free, contains peppermint and other essential oils and is safe for the entire family. Label should be simple, modern and high end looking. Fun is good too if it looks nice!

Target Market(s)

Kids and Adults

Industry/Entity Type

Hair Care Product

Font styles to use
Sans Serif
Decorative

Requirements
Must have
• -Words that should be used: safe, non toxic, sulfate free, essential oils, pesticide free. - Naturally removes lice, super lice & nits are great words for the lice & nit eliminating mousse and treatment oil 100% Dimethicone oil
- On a side note there are no essential oils in the lice & nit eliminating mousse or treatment oil 100% Dimethicone oil
Nice to have
• Earth tone colors if possible
Kid safe, no fillers, colors or scents
100% effective (even against super lice)
8oz labels and 4oz labels
Should not have
• No pictures of lice

```html
<!DOCTYPE html>
<html lang="en">
<head>
<meta charset="utf-8">
<title>Green Willow Lice Removal – Label Range</title>
<link href="https://fonts.googleapis.com/css2?family=Oswald:wght@400;500;600&family=Raleway:wght@400;500&display=swap" rel="stylesheet">
<style>
  :root {
    --bg: #ffffff;
    --label: #f6f6f6;
    --ink: #3a3a3a;
    --ink-dark: #161616;
    --muted: #555555;
    --orange-light: #f0a070;
    --orange: #e8622f;
    --orange-dark: #c8321a;
    --purple-light: #d3a9d6;
    --purple: #b070b0;
    --purple-dark: #72246a;
    --teal-light: #6ccdb9;
    --teal: #3bb59c;
    --teal-dark: #0c8069;
    --blue-light: #bcdff3;
    --blue: #3c96d4;
    --blue-dark: #7bb6df;
    --grey-light: #6a6a6a;
    --grey: #333333;
    --grey-dark: #111111;
    --oil-orange: #e2562a;
  }
  * { box-sizing: border-box; margin: 0; padding: 0; }
  html, body { width: 1200px; height: 1200px; overflow: hidden; background: var(--bg); }
  .range {
    width: 1200px; height: 1200px;
    display: flex; align-items: center; justify-content: center; gap: 24px;
  }
  .label {
    width: 212px; height: 430px;
    background: var(--label);
    display: flex; flex-direction: column; align-items: center;
    padding-top: 22px;
    font-family: "Raleway", sans-serif;
    color: var(--ink);
    border-radius: 4px;
  }
  .label--shampoo { --a: var(--orange); --a-light: var(--orange-light); --a-dark: var(--orange-dark); }
  .label--conditioner { --a: var(--purple); --a-light: var(--purple-light); --a-dark: var(--purple-dark); }
  .label--spray { --a: var(--teal); --a-light: var(--teal-light); --a-dark: var(--teal-dark); }
  .label--mousse { --a: var(--blue); --a-light: var(--blue-light); --a-dark: var(--blue-dark); }
  .label--oil { --a: var(--grey); --a-light: var(--grey-light); --a-dark: var(--grey-dark); }

  .category {
    width: 100%; display: flex; align-items: center; gap: 5px;
    font-size: 11px; font-weight: 500; letter-spacing: 0.2px; white-space: nowrap;
  }
  .category::before, .category::after {
    content: ""; flex: 1; height: 3px;
  }
  .category::before { background: var(--a-light); }
  .category::after { background: var(--a-dark); }
  .label--mousse .category::before, .label--mousse .category::after { background: var(--blue); }

  .brand { margin-top: 14px; display: flex; flex-direction: column; align-items: center; gap: 6px; }
  .brand-dot {
    width: 40px; height: 40px; border-radius: 50%;
    border: 1.5px solid #9a9a9a;
  }
  .brand-name {
    font-size: 8px; font-weight: 500; letter-spacing: 1.5px; color: var(--muted);
    text-align: center; width: 120px; line-height: 1.3;
  }

  .line {
    margin-top: 22px; font-size: 16px; color: var(--a); letter-spacing: 0.3px; text-align: center;
  }
  .label--oil .line { color: var(--ink); }
  .label--mousse .line { font-size: 17px; line-height: 1.15; margin-top: 16px; }

  .product {
    font-family: "Oswald", sans-serif; font-weight: 500;
    font-size: 34px; line-height: 1; margin-top: 12px;
    color: var(--ink); letter-spacing: -0.3px; text-align: center;
    transform: scaleX(0.92);
  }
  .product--oil {
    font-size: 22px; line-height: 1.15; color: var(--oil-orange); font-weight: 400;
  }
  .claim { margin-top: 10px; font-size: 12.5px; color: var(--a); text-align: center; }
  .label--oil .claim { color: var(--ink); }
  .note { margin-top: 3px; font-size: 10px; color: var(--ink); text-align: center; }

  .kid-safe {
    margin-top: 12px; background: var(--ink-dark); color: #fff;
    font-family: "Oswald", sans-serif; font-size: 12px; letter-spacing: 0.3px;
    padding: 2px 9px; border-radius: 12px;
  }

  .dots { margin-top: 14px; width: 100%; border-top: 2px dotted #9a9a9a; }
  .claims-strip {
    margin-top: 6px; width: 100%; text-align: center; white-space: nowrap; overflow: hidden;
    font-family: "Oswald", sans-serif; font-size: 7.5px; letter-spacing: 0.2px; color: var(--a);
  }
  .claims-strip b { font-weight: 600; color: var(--a-dark); }
  .label--mousse .claims-strip b { color: var(--blue); }
  .label--oil .claims-strip { color: var(--ink); }

  .netwt {
    margin-top: 5px; width: 100%; height: 38px;
    display: flex; align-items: center; justify-content: center;
    background: linear-gradient(90deg, var(--a) 0%, var(--a-light) 25%, var(--a) 60%, var(--a-dark) 100%);
    color: #fff; font-size: 10px; letter-spacing: 0.2px;
  }
  .label--mousse .netwt {
    background: linear-gradient(90deg, var(--blue-light) 0%, #cfe7f5 40%, var(--blue-dark) 100%);
    color: var(--ink);
  }
</style>
</head>
<body>
<main class="range">

  <section class="label label--shampoo">
    <div class="category">LICE PREVENTION</div>
    <div class="brand"><span class="brand-dot"></span><span class="brand-name">GREEN WILLOW LICE REMOVAL</span></div>
    <p class="line">· MINT REPEL ·</p>
    <h2 class="product">SHAMPOO</h2>
    <p class="claim">PROVEN EFFECTIVE</p>
    <p class="note">(natural lice repellent)</p>
    <span class="kid-safe">Kid safe!</span>
    <div class="dots"></div>
    <p class="claims-strip">NON TOXIC • SULFATE FREE • <b>ESSENTIAL OILS</b> • PESTICIDE FREE</p>
    <div class="netwt">NET.WT. 8 OZ</div>
  </section>

  <section class="label label--conditioner">
    <div class="category">LICE PREVENTION</div>
    <div class="brand"><span class="brand-dot"></span><span class="brand-name">GREEN WILLOW LICE REMOVAL</span></div>
    <p class="line">· MINT REPEL ·</p>
    <h2 class="product">CONDITIONER</h2>
    <p class="claim">PROVEN EFFECTIVE</p>
    <p class="note">(natural lice repellent)</p>
    <span class="kid-safe">Kid safe!</span>
    <div class="dots"></div>
    <p class="claims-strip">NON TOXIC • SULFATE FREE • <b>ESSENTIAL OILS</b> • PESTICIDE FREE</p>
    <div class="netwt">NET.WT. 8 OZ</div>
  </section>

  <section class="label label--spray">
    <div class="category">LICE PREVENTION</div>
    <div class="brand"><span class="brand-dot"></span><span class="brand-name">GREEN WILLOW LICE REMOVAL</span></div>
    <p class="line">· MINT REPEL ·</p>
    <h2 class="product">MINT SPRAY</h2>
    <p class="claim">PROVEN EFFECTIVE</p>
    <p class="note">(natural lice repellent)</p>
    <span class="kid-safe">Kid safe!</span>
    <div class="dots"></div>
    <p class="claims-strip">NON TOXIC • SULFATE FREE • <b>ESSENTIAL OILS</b> • PESTICIDE FREE</p>
    <div class="netwt">NET.WT. 8 OZ</div>
  </section>

  <section class="label label--mousse">
    <div class="category">LICE TREATMENT</div>
    <div class="brand"><span class="brand-dot"></span><span class="brand-name">GREEN WILLOW LICE REMOVAL</span></div>
    <p class="line">· LICE &amp; NIT ·<br>ELIMINATING</p>
    <h2 class="product">MOUSSE</h2>
    <p class="claim">PROVEN EFFECTIVE</p>
    <p class="note">(dissolves nit glue)</p>
    <span class="kid-safe">Kid safe!</span>
    <div class="dots"></div>
    <p class="claims-strip">NON TOXIC • SULFATE FREE • <b>NO CHEMICALS</b> • PESTICIDE FREE</p>
    <div class="netwt">NET.WT. 8 OZ</div>
  </section>

  <section class="label label--oil">
    <div class="category">LICE TREATMENT</div>
    <div class="brand"><span class="brand-dot"></span><span class="brand-name">GREEN WILLOW LICE REMOVAL</span></div>
    <p class="line">· LICE ELIMINATOR ·</p>
    <h2 class="product product--oil">100%<br>DIMETHICONE OIL</h2>
    <p class="claim">PROVEN EFFECTIVE</p>
    <p class="note">(even against super lice)</p>
    <span class="kid-safe">Kid safe!</span>
    <div class="dots"></div>
    <p class="claims-strip">NON TOXIC • SULFATE FREE • <b>NO CHEMICALS</b> • PESTICIDE FREE</p>
    <div class="netwt">NET.WT. 8 OZ</div>
  </section>

</main>
</body>
</html>
```